Business card design for Tolvin Waste

I would like double-sided business cards for myself and my partner that includes our logo and the existing colour scheme. We provide waste and environmental services to customers in the motor-vehicle and engineering industries.

```html
<!DOCTYPE html>
<html lang="en">
<head>
<meta charset="utf-8">
<title>Tolvin Waste – Business Card</title>
<link href="https://fonts.googleapis.com/css2?family=Open+Sans:wght@400;600;700&display=swap" rel="stylesheet">
<style>
  :root {
    --backdrop: #e8e9eb;
    --card-white: #fbfbfb;
    --lime-light: #b7da4c;
    --lime-dark: #9fcb3a;
    --leaf-deep: #6b9c3c;
    --leaf-mid: #7fb241;
    --leaf-faint: #dfe6d6;
    --ink: #3b3d40;
    --ink-soft: #55585c;
  }
  * { box-sizing: border-box; margin: 0; padding: 0; }
  html, body {
    width: 1200px;
    height: 1200px;
    overflow: hidden;
    background: var(--backdrop);
    font-family: "Open Sans", Arial, sans-serif;
  }
  .canvas {
    position: relative;
    width: 1200px;
    height: 1200px;
  }
  .card {
    position: absolute;
    left: 293px;
    width: 643px;
    height: 367px;
    overflow: hidden;
  }
  .card--front {
    top: 187px;
    background: linear-gradient(180deg, var(--lime-light) 0%, var(--lime-dark) 100%);
  }
  .card--back {
    top: 648px;
    background: var(--card-white);
  }
  .edge-ring {
    position: absolute;
  }
  .card--front .edge-ring {
    right: -150px;
    top: 38px;
    width: 300px;
    height: 300px;
    border: 14px solid var(--leaf-mid);
    border-radius: 50%;
    opacity: 0.75;
  }
  .card--back .edge-ring {
    left: -272px;
    top: 24px;
    width: 320px;
    height: 320px;
    border: 14px solid var(--leaf-faint);
    border-radius: 50%;
  }
  .brand {
    position: absolute;
    display: flex;
    align-items: center;
    gap: 14px;
  }
  .card--front .brand { left: 74px; top: 150px; }
  .card--back .brand { left: 72px; top: 152px; }
  .brand__dot {
    width: 54px;
    height: 54px;
    border-radius: 50%;
    border: 5px solid var(--leaf-deep);
    flex: none;
  }
  .card--back .brand__dot { border-color: var(--leaf-mid); }
  .brand__name {
    display: flex;
    flex-direction: column;
    font-weight: 700;
    font-size: 28px;
    line-height: 32px;
    letter-spacing: 2px;
    text-transform: uppercase;
    color: var(--leaf-deep);
    white-space: nowrap;
  }
  .card--back .brand__name { color: var(--ink); }
  .contact {
    position: absolute;
    left: 354px;
    top: 84px;
    color: var(--ink-soft);
  }
  .contact__name {
    font-size: 24px;
    font-weight: 400;
    color: var(--ink);
    line-height: 1.1;
  }
  .contact__role {
    font-size: 9px;
    font-weight: 600;
    letter-spacing: 0.5px;
    text-transform: uppercase;
    color: var(--leaf-mid);
    margin-top: 3px;
  }
  .contact__list {
    list-style: none;
    margin-top: 28px;
  }
  .contact__item {
    display: flex;
    align-items: flex-start;
    gap: 10px;
    font-size: 15px;
    line-height: 19px;
    margin-bottom: 9px;
  }
  .contact__icon {
    width: 17px;
    height: 17px;
    flex: none;
    margin-top: 1px;
  }
</style>
</head>
<body>
<main class="canvas">

  <section class="card card--front" aria-label="Card front">
    <div class="edge-ring"></div>
    <div class="brand">
      <span class="brand__dot"></span>
      <span class="brand__name"><span>Tolvin</span><span>Waste</span></span>
    </div>
  </section>

  <section class="card card--back" aria-label="Card back">
    <div class="edge-ring"></div>
    <div class="brand">
      <span class="brand__dot"></span>
      <span class="brand__name"><span>Tolvin</span><span>Waste</span></span>
    </div>

    <div class="contact">
      <p class="contact__name">First Last Name</p>
      <p class="contact__role">Position Head</p>
      <ul class="contact__list">
        <li class="contact__item">
          <svg class="contact__icon" viewBox="0 0 20 20" aria-hidden="true">
            <circle cx="10" cy="10" r="9" fill="none" stroke="#7fb241" stroke-width="1.5"/>
            <rect x="7.5" y="5" width="5" height="10" rx="1" fill="none" stroke="#7fb241" stroke-width="1.4"/>
          </svg>
          <span>418 620 7394</span>
        </li>
        <li class="contact__item">
          <svg class="contact__icon" viewBox="0 0 20 20" aria-hidden="true">
            <circle cx="10" cy="10" r="9" fill="#7fb241"/>
            <rect x="5" y="6.5" width="10" height="7" rx="1" fill="#fff"/>
            <path d="M5 7 L10 11 L15 7" fill="none" stroke="#7fb241" stroke-width="1.2"/>
          </svg>
          <span>hello@tolvinwaste.com</span>
        </li>
        <li class="contact__item">
          <svg class="contact__icon" viewBox="0 0 20 20" aria-hidden="true">
            <circle cx="10" cy="10" r="9" fill="none" stroke="#7fb241" stroke-width="1.5"/>
            <ellipse cx="10" cy="10" rx="3.5" ry="7" fill="none" stroke="#7fb241" stroke-width="1.2"/>
            <line x1="3" y1="10" x2="17" y2="10" stroke="#7fb241" stroke-width="1.2"/>
          </svg>
          <span>www.tolvinwaste.com</span>
        </li>
        <li class="contact__item">
          <svg class="contact__icon" viewBox="0 0 20 20" aria-hidden="true">
            <circle cx="10" cy="10" r="9" fill="none" stroke="#7fb241" stroke-width="1.5"/>
            <path d="M10 15 C7 11 6.5 9.5 6.5 8.3 A3.5 3.5 0 0 1 13.5 8.3 C13.5 9.5 13 11 10 15Z" fill="#7fb241"/>
            <circle cx="10" cy="8.3" r="1.3" fill="#fff"/>
          </svg>
          <span>4120 Harbour Court<br>Millbrook Lane<br>3181 Victoria<br>Australia.</span>
        </li>
      </ul>
    </div>
  </section>

</main>
</body>
</html>
```